Wine labels Velmora Wine Council - Nueva etiqueta El Consejo Regulador de vinos de Albarrán

Velmora Wines Council, based in southern Spain, are looking to create a new suite of wine labels which retain the elegance of the Velmora Wines industry while reinvigorating their image to the modern era and a new generation of Sherry Wine lovers. These labels will be used across the Velmora Wines Council's range of wines for the promotion of the Velmora Wines industry.

Your design must present at least two styles of Velmora Wines which demonstrate an elegant, modern interpretation and understanding of the unique mood and personality for these wines and the essence of southern Spain.

10 labels will be created based on the winning design, one for each of the unique varieties of Velmora Wines within the collection. This collection comprises of several different wine varieties including: Fino, Manzanilla, Amontillado, Oloroso, Palo Cortado, Medium, Cream, Pale Cream, Pedro Ximenez and Moscatel.

We recommend you visit our website www.velmora-vinos.example/wines as the source to understanding the origins and unique personality of these diverse wines.

El Consejo Regulador de los Vinos de Albarrán y Tordesal quiere renovar las etiquetas de los vinos utilizados para sus actividades de promoción genérica. Esta colección de vinos comprende las tipologías más importantes de la región que incluye: fino, manzanilla, amontillado, oloroso, palo cortado, pale cream, medium, cream, pedro ximénez y moscatel. Por lo tanto se precisan 10 etiquetas, una para cada uno de los vinos mencionados.
Updates

Project Deadline Extended
Reason: Due to some confusion with the deadline we wish to officially extend the deadline to allow designers one last week to submit their entries.

Target Market(s)

Industry, journalists, media, sommeliers, chefs, wine writers

Industry/Entity Type

Council

Requirements
Must have
• Front and Back label plus capsule:
• Front label can have either of the two official logos of the Velmora Wine council titled Vinos de Albarrán Digital or not, this is optional. Must include: Vino selecionado por el Consejo Regulador de la Denominacion de Origen, Name of the variety of wine eg FINO, percentage of alcohol eg 15% and quantity 75 cl.
• The back of the label must include the council logo titled Sellora and 4 additional logos positioned smaller. The Europa logo must appear larger than the 3 other logos. Space for descriptive text about the wine is also required.
• The dimensions of the bottle can be found at this link http://www.vidrialto.example/es/catalogo/vinos-y-espumosos/bordelesas/bd-orla
• Altura:305 mm
• Diámetro base:76,20 mm
• Diámetro hombro:82 mm
• Tipo boca:Cetie
• Peso:750 gr
• Capacidad:75 cl
• Etiqueta delantera y trasera y capsula
• La etiqueta delantera puede incluir el logo oficial del Consejo Regulador o el logo digital, o ninguno, esto es opcional. Debe incluir el siguiete texto: Vino selecionado por el Consejo Regulador de la Denominacion de Origen, el nombre de la variedad del vino, por ejemplo Fino, el porcentaje de alcohol, por ejemplo 15%, y la capacidad 75cl.
• La etiqueta trasera debe incluir el logo oficial Sellora del Consejo, y cuatro logos adicionales con una dimension menor. El Logo de ¨Europa invierte en las zonas rurales¨ debe ser de mayor tamaño que los otros. Se precisa espacio para el texto descriptivo de los vinos.
• Las dimensiones de la botella se puede encontrar en este enlace
• http://www.vidrialto.example/es/catalogo/vinos-y-espumosos/bordelesas/bd-orla
• Altura:305 mm
• Diámetro base:76,20 mm
• Diámetro hombro:82 mm
• Tipo boca:Cetie
• Peso:750 gr
• Capacidad:75 cl
Nice to have
• See our website velmora-vinos.example to understand the origin of the wines. Ver nuestra página web velmora-vinos.example para mejor entender los vinos.
Should not have
• Images of catavinos or stereotypical images from Spain such as flamenco dancers or guitars.

```html
<!DOCTYPE html>
<html lang="es">
<head>
<meta charset="utf-8">
<title>Vinos de Albarrán – Oloroso</title>
<link href="https://fonts.googleapis.com/css2?family=Cinzel:wght@500&family=Playfair+Display:wght@400&family=Montserrat:wght@500;600&family=Old+Standard+TT:wght@400;700&display=swap" rel="stylesheet">
<style>
  :root{
    --bg-light:#ffffff;
    --bg-edge:#c9c9cb;
    --capsule:#31241b;
    --gold:#e5a21c;
    --label-paper:#ddd5cf;
    --maroon:#6e1a2c;
    --ink:#2e241f;
  }
  *{box-sizing:border-box;margin:0;padding:0}
  html,body{width:1200px;height:1200px;overflow:hidden}
  body{
    position:relative;
    background:radial-gradient(ellipse at 50% 55%, var(--bg-light) 35%, var(--bg-edge) 100%);
    font-family:"Old Standard TT", serif;
  }
  .capsule{
    position:absolute;left:522px;top:160px;width:170px;height:150px;
    background:var(--capsule);
  }
  .capsule__frame{
    position:absolute;left:26px;top:40px;width:118px;height:70px;
    border:2px solid var(--gold);
    display:flex;align-items:center;justify-content:center;
    font-family:"Cinzel", serif;color:var(--gold);font-size:13px;letter-spacing:2.5px;
  }
  .label{
    position:absolute;left:398px;top:383px;width:418px;height:656px;
    background:var(--label-paper);overflow:hidden;
  }
  .label__scene{
    position:absolute;left:0;right:0;top:290px;bottom:0;
    background:
      radial-gradient(ellipse 60px 110px at 340px 240px, rgba(200,200,200,.55), rgba(200,200,200,0) 100%),
      radial-gradient(ellipse 90px 70px at 60px 200px, rgba(70,70,70,.45), rgba(70,70,70,0) 100%),
      radial-gradient(ellipse 110px 60px at 120px 330px, rgba(60,60,60,.5), rgba(60,60,60,0) 100%),
      radial-gradient(ellipse 120px 50px at 230px 250px, rgba(180,180,180,.5), rgba(180,180,180,0) 100%),
      linear-gradient(to bottom, rgba(160,160,160,0) 0%, rgba(165,165,165,.55) 28%, #9a9a9a 55%, #8c8c8c 80%, #7a7a7a 100%);
  }
  .label__band{
    position:absolute;left:0;right:0;top:546px;height:31px;
    background:var(--gold);opacity:.72;
  }
  .label__frame{
    position:absolute;left:11px;top:14px;right:16px;bottom:11px;
    border:1.5px solid var(--maroon);
  }
  .label__frame--inner{left:18px;top:20px;right:22px;bottom:17px;border-width:1px}
  .corner{
    position:absolute;width:44px;height:44px;
    background:radial-gradient(circle at 50% 50%, rgba(110,26,44,.28), rgba(110,26,44,0) 70%);
  }
  .corner--tl{left:6px;top:8px}.corner--tr{right:10px;top:8px}
  .corner--bl{left:6px;bottom:6px}.corner--br{right:10px;bottom:6px}
  .brand{
    position:absolute;left:0;right:0;top:200px;text-align:center;
    font-family:"Playfair Display", serif;color:var(--ink);font-size:30px;letter-spacing:-1px;line-height:1;
  }
  .brand__sub{
    position:absolute;left:0;right:0;top:239px;text-align:center;
    font-family:"Montserrat", sans-serif;font-weight:500;color:var(--ink);font-size:12.5px;letter-spacing:3px;
  }
  .crest{
    position:absolute;left:136px;width:148px;height:50px;
  }
  .crest--top{top:298px;background:radial-gradient(ellipse 50% 100% at 50% 100%, rgba(110,26,44,.32), rgba(110,26,44,0) 100%)}
  .crest--bottom{top:425px;background:radial-gradient(ellipse 50% 100% at 50% 0%, rgba(110,26,44,.32), rgba(110,26,44,0) 100%)}
  .rule{
    position:absolute;top:381px;width:36px;height:12px;
    background:repeating-linear-gradient(to bottom, var(--gold) 0 2px, transparent 2px 5px);
  }
  .rule--left{left:64px}.rule--right{left:318px}
  .variety{
    position:absolute;left:99px;top:348px;width:220px;height:77px;
    background:var(--maroon);padding:13px;
  }
  .variety__inner{
    width:100%;height:100%;background:var(--label-paper);border:1.5px solid var(--gold);
    display:flex;align-items:center;justify-content:center;
    font-size:19px;letter-spacing:3px;color:var(--ink);
  }
  .seal{
    position:absolute;left:123px;top:521px;width:170px;height:84px;
    background:var(--maroon);padding:5px;
  }
  .seal__inner{
    width:100%;height:100%;background:var(--label-paper);
    text-align:center;padding-top:14px;color:var(--ink);font-size:6.5px;line-height:1.35;letter-spacing:.6px;
  }
  .seal__council{font-family:"Montserrat", sans-serif;font-weight:600;color:var(--maroon);font-size:9px;letter-spacing:1px}
  .seal__rule{width:100px;margin:3px auto 4px;border-top:1px solid var(--ink)}
  .seal__specs{color:var(--maroon);font-weight:700}
</style>
</head>
<body>
  <div class="capsule">
    <div class="capsule__frame">ALBARRÁN</div>
  </div>

  <section class="label">
    <div class="label__scene" role="img" aria-label="Greyscale vineyard scene with grape clusters"></div>
    <div class="label__band"></div>
    <div class="label__frame"></div>
    <div class="label__frame label__frame--inner"></div>
    <div class="corner corner--tl" role="img" aria-label="Corner flourish ornament"></div>
    <div class="corner corner--tr" role="img" aria-label="Corner flourish ornament"></div>
    <div class="corner corner--bl" role="img" aria-label="Corner flourish ornament"></div>
    <div class="corner corner--br" role="img" aria-label="Corner flourish ornament"></div>

    <div class="brand">VINOS DE ALBARRÁN</div>
    <div class="brand__sub">VELMORA WINES</div>

    <div class="crest crest--top" role="img" aria-label="Filigree ornament above variety plaque"></div>
    <div class="crest crest--bottom" role="img" aria-label="Filigree ornament below variety plaque"></div>
    <div class="rule rule--left"></div>
    <div class="rule rule--right"></div>
    <div class="variety"><div class="variety__inner">OLOROSO</div></div>

    <div class="seal">
      <div class="seal__inner">
        <div>Vino selecionado por el</div>
        <div class="seal__council">CONSEJO REGULADOR</div>
        <div>de la Denominacion de Origen</div>
        <div class="seal__rule"></div>
        <div class="seal__specs">75 cL &nbsp;-&nbsp; 15% voL</div>
      </div>
    </div>
  </section>
</body>
</html>
```